Brochure design for Velicor

Create a bi-fold A5 size brochure. I have attached our logo and the written content to be included in the brochure. So the brochure will have a total of 4 pages (front page, inner two pages, back page). End source files need to include final printable brochure as well as editable files.

```html
<!DOCTYPE html>
<html lang="en">
<head>
<meta charset="utf-8">
<title>Velicor – Bi-fold Brochure</title>
<link href="https://fonts.googleapis.com/css2?family=Quicksand:wght@300;400;500;700&display=swap" rel="stylesheet">
<style>
  :root{
    --stage:#5f5f61;
    --charcoal:#3b3b3d;
    --charcoal-deep:#323234;
    --blue:#3a5e9e;
    --green:#8cc63f;
    --green-dark:#5a9a3a;
    --paper:#ffffff;
    --ink:#4a4a4a;
    --rule:#9cc56a;
    --ref-row:#dcdcdc;
  }
  *{margin:0;padding:0;box-sizing:border-box;}
  html,body{width:893px;height:1200px;overflow:hidden;background:var(--stage);}
  body{font-family:"Quicksand",sans-serif;color:var(--ink);}
  .board{position:absolute;left:0;top:0;width:1116px;height:1500px;transform:scale(.8);transform-origin:0 0;}
  .page{position:absolute;overflow:hidden;box-shadow:0 2px 6px rgba(0,0,0,.25);}
  .page svg.art{position:absolute;left:0;top:0;}

  /* outer spread */
  .back-cover{left:110px;top:103px;width:448px;height:633px;background:var(--charcoal);}
  .back-cover .footer-band{position:absolute;left:0;bottom:0;width:100%;height:99px;background:var(--charcoal-deep);}
  .brand{position:absolute;display:flex;align-items:center;gap:6px;}
  .brand .mark{width:18px;height:18px;background:var(--green);}
  .brand .name{font-weight:700;font-size:30px;color:var(--green);line-height:1;}
  .brand .tagline{position:absolute;left:24px;top:32px;font-size:7px;color:var(--green);white-space:nowrap;}
  .back-cover .brand{left:146px;top:440px;}
  .contacts{position:absolute;left:0;width:100%;top:560px;text-align:center;color:#fff;font-size:9px;line-height:11px;}
  .contacts strong{font-weight:700;}

  .front-cover{left:558px;top:103px;width:449px;height:633px;background:linear-gradient(180deg,#fafafa,#ececec);}
  .front-cover .brand-box{position:absolute;left:29px;top:32px;width:134px;height:57px;background:#e2e2e2;}
  .front-cover .brand{left:10px;top:13px;}
  .front-cover .brand .name{font-size:24px;}
  .front-cover .brand .tagline{top:27px;font-size:6px;}
  .headline{position:absolute;left:54px;top:307px;color:#fff;font-size:17px;line-height:19px;letter-spacing:1px;text-transform:uppercase;font-weight:300;}
  .headline b{font-weight:700;}
  .subline{position:absolute;left:54px;top:461px;color:rgba(255,255,255,.82);font-size:14.5px;line-height:19px;letter-spacing:.8px;text-transform:uppercase;font-weight:300;}
  .web-band{position:absolute;right:22px;top:605px;color:#fff;font-size:14px;font-weight:700;letter-spacing:4.5px;}

  /* inner spread */
  .inner-left{left:110px;top:765px;width:448px;height:634px;background:linear-gradient(90deg,#f4f4f4,#fff 40%);}
  .topic{position:absolute;left:40px;width:368px;}
  .topic h2{font-size:12px;font-weight:400;color:var(--blue);letter-spacing:.4px;padding-bottom:6px;border-bottom:1px solid var(--rule);}
  .topic h2 b{color:var(--green-dark);font-weight:500;}
  .topic p{margin-top:10px;font-size:6px;line-height:8.2px;text-align:justify;color:#555;}

  .inner-right{left:558px;top:765px;width:449px;height:634px;background:linear-gradient(180deg,#f6f6f6,#e9e9e9);}
  .info{position:absolute;left:180px;top:35px;width:240px;text-align:center;color:#fff;font-size:7.2px;line-height:9.8px;}
  .info p{margin-bottom:10px;}
  .info b{font-weight:700;}
  .refs{position:absolute;left:40px;top:450px;width:370px;list-style:none;}
  .refs li{display:flex;align-items:center;min-height:11px;margin-bottom:2px;background:var(--ref-row);font-size:5.2px;line-height:6px;color:#555;}
  .refs li span.num{flex:none;width:12px;height:11px;margin-right:6px;background:var(--green-dark);color:#fff;font-size:5px;display:flex;align-items:center;justify-content:center;}
</style>
</head>
<body>
<div class="board">

  <section class="page back-cover">
    <div class="footer-band"></div>
    <div class="brand"><span class="mark"></span><span class="name">velicor</span><span class="tagline">Personalised Health &amp; Wellness</span></div>
    <div class="contacts">
      <strong>Business Contacts:</strong><br>
      +49 (30) 555 014 220<br>
      booking@northwingair.com<br>
      www.northwingair.com
    </div>
  </section>

  <section class="page front-cover">
    <svg class="art" width="449" height="633" viewBox="0 0 449 633">
      <defs>
        <linearGradient id="brandGrad" x1="0" y1="0.3" x2="1" y2="0.7">
          <stop offset="0" stop-color="#3a5e9e"/>
          <stop offset="0.5" stop-color="#4f8f7a"/>
          <stop offset="1" stop-color="#8cc63f"/>
        </linearGradient>
        <linearGradient id="labGrad" x1="0" y1="0" x2="1" y2="1">
          <stop offset="0" stop-color="#e8eef2"/>
          <stop offset="0.6" stop-color="#b9c9d3"/>
          <stop offset="1" stop-color="#8fa3b0"/>
        </linearGradient>
      </defs>
      <polygon points="0,280 215,62 449,450 449,633 0,633" fill="url(#brandGrad)"/>
      <g role="img" aria-label="Laboratory photograph of a pipette above glass sample dishes, shown in rounded diamond tiles">
        <rect x="-85" y="-85" width="170" height="170" rx="14" transform="translate(350,110) rotate(45)" fill="url(#labGrad)" stroke="#fff" stroke-width="6"/>
        <rect x="-50" y="-50" width="100" height="100" rx="10" transform="translate(190,170) rotate(45)" fill="url(#labGrad)" stroke="#fff" stroke-width="6"/>
        <rect x="-50" y="-50" width="100" height="100" rx="10" transform="translate(290,245) rotate(45)" fill="url(#labGrad)" stroke="#fff" stroke-width="6"/>
      </g>
      <rect x="-26" y="-26" width="52" height="52" rx="7" transform="translate(62,160) rotate(45)" fill="url(#brandGrad)"/>
      <rect x="-16" y="-16" width="32" height="32" rx="4" transform="translate(410,242) rotate(45)" fill="url(#brandGrad)"/>
      <polygon points="222,592 449,592 449,633 182,633" fill="#2f2f31"/>
    </svg>
    <div class="brand-box">
      <div class="brand"><span class="mark"></span><span class="name">velicor</span><span class="tagline">Personalised Health &amp; Wellness</span></div>
    </div>
    <h1 class="headline">A <b>Revolution</b><br><b>in Health &amp;</b><br><b>Wellness</b><br>has been<br>brewing<br>– and <b>now</b><br><b>it is here!</b></h1>
    <p class="subline">Precision health<br>and wellness is<br>tailored to your<br>unique genetic<br>make-up.</p>
    <div class="web-band">www.velicor.co</div>
  </section>

  <section class="page inner-left">
    <article class="topic" style="top:38px">
      <h2>Precision <b>Health &amp; Wellness</b></h2>
      <p>You are unique. Your healthcare and lifestyle decisions need to be tailored to you. Ever since the human genome was decoded, a plethora of scientific data has revealed everything from disease-causing genes to genetically tailored diets. We all want to live longer and healthier lives, whilst performing at our peak. One size does not fit all and the only way to find out what's right for you is to unlock your hidden code.</p>
    </article>
    <article class="topic" style="top:110px">
      <h2>DNA – <b>The Code of Life</b></h2>
      <p>Every individual living organism has a completely unique set of DNA. Your DNA is the chemical blueprint that codes for everything in your body and is found in all of the trillions of cells that you are made of. Collections of DNA are called genes and the complete set of genes in an individual is referred to as their genome. The human genome was first decoded in 2003, taking over 13 years and $2.7 billion to complete. Thanks to exponential advances in technology, Velicor can now unlock your DNA for only a fraction of the time and cost.</p>
    </article>
    <article class="topic" style="top:190px">
      <h2>Unlock <b>Your Hidden Code</b></h2>
      <p>A whole new world of discovery awaits with the Velicor range of genetic testing services. From unlocking your complete genome with Whole Genome Sequencing (WGS) to just learning about specific aspects of what makes you... you. With Velicor, you can find answers to the questions that can help you to live a healthier, longer and optimal quality of life.</p>
    </article>
    <article class="topic" style="top:262px">
      <h2>DNA <b>&amp; Disease</b></h2>
      <p>Prevention is better than any cure. Scientific studies have uncovered numerous genes associated with a range of cancers, heart conditions, and other common diseases affecting society today. The range of genetic tests available through Velicor can now identify if these, and other, genes are present in you. This allows you and your physician to potentially prevent, manage, monitor and treat relevant conditions. Furthermore, as the rapid pace of science continues to uncover new genes related to disease, Velicor can quickly update you and your doctor with the latest research and what it means for you.</p>
    </article>
    <article class="topic" style="top:351px">
      <h2>DNA <b>&amp; Drugs</b></h2>
      <p>Scientific research has shown that the response rate for many prescribed drugs is as low as 50% and that genetic factors can account for up to 95% of drug-response variability and susceptibility. In other words, many of the drugs you take in your lifetime will likely be inadequately dosed, leading to potential side effects or no effects at all. With Velicor, you and your doctor can proactively identify appropriate types, and dosages, for a range of prescribed and over-the-counter medications. This includes medications you currently take and any common future medications you are likely to encounter at some stage in your life. A number of studies have shown that over 74% of people taking a genetic test for medication compatibility learned information that is relevant to them.</p>
    </article>
    <article class="topic" style="top:455px">
      <h2>DNA <b>&amp; Diet</b></h2>
      <p>Certain foods are thought to inappropriately cause immune reactions in genetically predisposed individuals. This can result in symptoms like fatigue, bloating, bowel disturbances, headaches, migraines, joint aches, eczema or acne. DNA testing can help identify such foods as well as genes associated with the metabolism and absorption of vitamins, minerals and stimulants like coffee. The Velicor range of tests can even help create precision diet and fitness plans based on your genes and goals.</p>
    </article>
    <article class="topic" style="top:535px">
      <h2>DNA <b>&amp; Descent</b></h2>
      <p>The discipline of genealogy has exploded over recent years with the advent of DNA testing. The Velicor range of tests can help you track and understand your ancestry and paternity tests can help identify an individual's biological father. Family planning tests can help identify a couple's risk profile for conceiving children with any of the dozens of known genetic conditions that can affect humans.</p>
    </article>
  </section>

  <section class="page inner-right">
    <svg class="art" width="449" height="634" viewBox="0 0 449 634">
      <defs>
        <linearGradient id="sunGrad" x1="0" y1="0" x2="1" y2="1">
          <stop offset="0" stop-color="#e9d2a8"/>
          <stop offset="0.5" stop-color="#b58a5c"/>
          <stop offset="1" stop-color="#6d5a48"/>
        </linearGradient>
        <linearGradient id="panelGrad" x1="0" y1="0" x2="1" y2="0.6">
          <stop offset="0" stop-color="#3a5e9e"/>
          <stop offset="0.55" stop-color="#5b9a6e"/>
          <stop offset="1" stop-color="#8cc63f"/>
        </linearGradient>
      </defs>
      <rect x="0" y="0" width="449" height="410" fill="url(#sunGrad)" role="img" aria-label="Photograph of friends standing with bicycles on a sunny day"/>
      <polygon points="0,0 26,0 0,26" fill="#3a5e9e"/>
      <polygon points="8,0 449,0 449,295 382,360" fill="url(#panelGrad)" opacity="0.95"/>
      <polygon points="120,634 300,450 449,560 449,634" fill="#e4e4e4"/>
    </svg>
    <div class="info">
      <p>For more information about Velicor<br>or<br>our products, please talk to your local retailer<br>or<br>email us at<br><b>enquiries@velicor.co</b></p>
      <p>Please note test availability may differ<br>from region to region and is subject to availability.</p>
      <p>Please talk to your local retailer for more information.<br>For a list of approved Velicor retailers</p>
      <p>please visit www.velicor.co</p>
    </div>
    <ol class="refs">
      <li><span class="num">01</span>Sample reference note: genome sequencing project summary, placeholder entry.</li>
      <li><span class="num">02</span>Author A, et al. Placeholder study on gene-guided prescribing. Sample Review.</li>
      <li><span class="num">03</span>Author B, et al. Placeholder overview of drug response genetics.</li>
      <li><span class="num">04</span>Author C, et al. Placeholder note on diagnostic gene panels.</li>
      <li><span class="num">05</span>Author D, et al. Placeholder study on medication dosing by genotype.</li>
      <li><span class="num">06</span>Author E, et al. Placeholder paper on personalised medicine uptake.</li>
      <li><span class="num">07</span>Author F, et al. Placeholder survey of patients after genetic testing.</li>
      <li><span class="num">08</span>Author G, et al. Placeholder trial of diet changes for bowel comfort.</li>
      <li><span class="num">09</span>Author H, et al. Placeholder trial of elimination diet for headaches.</li>
      <li><span class="num">10</span>Author J, et al. Placeholder study of food reactions in adults.</li>
      <li><span class="num">11</span>Author K, et al. Placeholder note on food-related joint aches.</li>
    </ol>
  </section>

</div>
</body>
</html>
```